Bright Current Electrical & Communications business card design

We would like a double sided business card that is different. Want it to be exciting and fun. Something that people keep rather then just throw it in the bin.
We have a logo that we want to put on one side of the business card and then the business information on the reverse side. Trying to go for a real professional style of business card

Target Market(s)

Electrical

Industry/Entity Type

Electrical

Contact Information for Business Card

Bright Current Electrical & Communications
Marcus Holloway
P: 0437 862 305
E: brightcurrent@mailbox-example.com.au
Lic No: 574106K
24/7

Font styles to use
Other font styles liked:
• Would like ideas

Requirements
Must have
• Our company logo (preferably on both sides) yellow needs to be incorporated somewhere. Business card card colours to match with logo. Maybe a small pop of colour
Nice to have
• Open to some design ideas

```html
<!DOCTYPE html>
<html lang="en">
<head>
<meta charset="utf-8">
<title>Bright Current Electrical &amp; Communications – Business Card</title>
<link href="https://fonts.googleapis.com/css2?family=Exo+2:wght@400;600;700&display=swap" rel="stylesheet">
<style>
  :root {
    --backdrop: #8a8c8b;
    --card: #e9eaec;
    --ink: #1d1d1f;
    --ink-soft: #6e6f72;
    --tab: #7b7c7e;
    --accent: #e8e04a;
  }
  * { box-sizing: border-box; margin: 0; padding: 0; }
  html, body {
    width: 1200px;
    height: 900px;
    overflow: hidden;
    background: var(--backdrop);
    font-family: "Exo 2", sans-serif;
  }
  .canvas { position: relative; width: 1200px; height: 900px; }
  .card {
    position: absolute;
    left: 321px;
    width: 507px;
    height: 290px;
    background: var(--card);
  }
  .card--front { top: 119px; }
  .card--back { top: 471px; }

  .brand-name {
    position: absolute;
    left: 0; right: 0;
    top: 108px;
    display: flex;
    flex-direction: column;
    align-items: center;
    color: var(--ink);
    font-weight: 700;
    text-transform: uppercase;
    letter-spacing: 0.04em;
    line-height: 1.2;
  }
  .brand-name__main { display: block; font-size: 28px; }
  .brand-name__sub-row {
    display: flex;
    align-items: center;
    width: 250px;
    gap: 8px;
    margin-top: 2px;
  }
  .brand-name__rule {
    flex: 1;
    height: 2px;
    background: var(--accent);
  }
  .brand-name__sub { font-size: 10px; letter-spacing: 0.08em; white-space: nowrap; }

  .side-tab {
    position: absolute;
    left: 0; top: 45px;
    width: 10px; height: 38px;
    background: var(--tab);
  }
  .holder-name {
    position: absolute;
    left: 44px; top: 42px;
    font-size: 22px;
    font-weight: 700;
    color: var(--ink);
  }
  .holder-role {
    position: absolute;
    left: 44px; top: 70px;
    font-size: 16px;
    color: var(--ink-soft);
  }
  .contact-list {
    position: absolute;
    left: 44px; top: 213px;
    list-style: none;
    font-size: 13px;
    line-height: 18px;
    color: var(--ink);
  }
  .contact-list__value { color: var(--ink-soft); letter-spacing: 0.03em; }
  .availability {
    position: absolute;
    left: 375px; top: 198px;
    width: 84px;
    text-align: center;
  }
  .availability svg { display: block; margin: 0 auto; }
  .licence {
    margin-top: 12px;
    font-size: 11px;
    color: var(--ink-soft);
  }
</style>
</head>
<body>
<main class="canvas">
  <section class="card card--front">
    <h1 class="brand-name">
      <span class="brand-name__main">Bright Current</span>
      <span class="brand-name__sub-row">
        <span class="brand-name__rule"></span>
        <span class="brand-name__sub">Electrical &amp; Communications</span>
        <span class="brand-name__rule"></span>
      </span>
    </h1>
  </section>

  <section class="card card--back">
    <div class="side-tab"></div>
    <h2 class="holder-name">Marcus Holloway</h2>
    <p class="holder-role">CEO/Founder</p>
    <ul class="contact-list">
      <li>Phone&nbsp; : <span class="contact-list__value">0437 862 305</span></li>
      <li>Email : <span class="contact-list__value">brightcurrent@mailbox-example.com.au</span></li>
      <li>Web : <span class="contact-list__value">www.brightcurrent-example.com</span></li>
    </ul>
    <div class="availability">
      <svg width="42" height="42" viewBox="0 0 42 42" aria-label="Open 24/7" role="img">
        <circle cx="21" cy="21" r="18.5" fill="none" stroke="#1d1d1f" stroke-width="3"/>
        <path d="M21 9 V22 L15 28" fill="none" stroke="#1d1d1f" stroke-width="2.5" stroke-linecap="round"/>
      </svg>
      <p class="licence">Lic No: 574106K</p>
    </div>
  </section>
</main>
</body>
</html>
```